Need simple and modern looking business card with all my information on one side and logo on the other side
Info :
Company name - VELMAR CONSTRUCTION LLC
Company addres- 418 harbor 87th. Dunmoor park ny 10352
Email- velmarllc@tridomail.Com
Company phone number 555-318-6094
Cell number- 555-742-0583
Web site - velmarllc.Com
My name Gerald tomasino

Target Market(s)

Construction , home improvement, remodeling

Industry/Entity Type

Construction

Contact Information for Business Card

It has to be moder but at the same time simple

Font styles to use
Sans Serif

Colors
0255a3
ffffff
000000
f78f20
b1b1b1
9d9d9d
1b1b1b
33a6d7
ec1f27

Requirements
Must have
• My logo on one side maybe with a some kind of background on the other side all my information
Nice to have
• Some kind of background pictures provided by you .PLEASE HAVE ACCOUNT WITH PIXELVAULT WILL NOT PAY ANY EXTRA FEES .
Should not have
• Any kind of hamer, nails,screws, helmets itp. Please do not copy the other designs come up with something new.

```html
<!DOCTYPE html>
<html lang="en">
<head>
<meta charset="utf-8">
<title>Velmar Construction LLC – Business Card</title>
<link href="https://fonts.googleapis.com/css2?family=Fira+Sans:wght@400;500;600&display=swap" rel="stylesheet">
<style>
  :root {
    --blue: #0255a3;
    --sky: #33a6d7;
    --orange: #f78f20;
    --red: #ec1f27;
    --rose: #c44a5a;
    --white: #ffffff;
    --black: #000000;
    --ink: #1b1b1b;
    --grey-light: #e6e6e8;
    --grey: #9d9d9d;
    --grey-dark: #5a5552;
    --backdrop: #e9e9e9;
  }
  * { margin: 0; padding: 0; box-sizing: border-box; }
  html, body { width: 1200px; height: 1200px; overflow: hidden; }
  body {
    background: var(--backdrop);
    font-family: "Fira Sans", Arial, sans-serif;
    color: var(--ink);
    position: relative;
  }
  .card {
    position: absolute;
    left: 150px;
    width: 900px;
    height: 514px;
    overflow: hidden;
    box-shadow: 0 10px 30px rgba(0,0,0,0.18);
  }
  .card--front { top: 70px; background: var(--white); }
  .card--back { top: 616px; }
  .card svg.bands { position: absolute; inset: 0; }

  .brand {
    position: absolute;
    display: flex;
    align-items: center;
    gap: 14px;
    font-weight: 600;
    color: var(--black);
  }
  .brand__mark { background: var(--orange); flex: none; }
  .brand__text { display: flex; flex-direction: column; line-height: 1; }

  .card--front .brand { left: 470px; top: 150px; }
  .card--front .brand__mark { width: 18px; height: 18px; }
  .card--front .brand__name { font-size: 58px; letter-spacing: 4px; }
  .card--front .brand__sub { font-size: 19px; letter-spacing: 3px; margin-top: 6px; }

  .holder { position: absolute; left: 70px; top: 310px; }
  .holder__name {
    color: var(--orange);
    font-weight: 500;
    font-size: 28px;
    text-transform: uppercase;
    letter-spacing: 0.5px;
  }
  .holder__cell { margin-top: 12px; font-size: 22px; color: #444; }

  .divider {
    position: absolute;
    left: 400px; top: 290px;
    width: 2px; height: 170px;
    background: var(--grey);
    opacity: 0.6;
  }

  .contacts {
    position: absolute;
    left: 430px; top: 282px;
    list-style: none;
    font-size: 22px;
    line-height: 35px;
    color: #333;
  }
  .contacts__label { color: var(--blue); font-weight: 500; margin-right: 6px; }

  .card--back .brand { left: 50%; top: 50%; transform: translate(-50%, -38%); }
  .card--back .brand__mark { width: 24px; height: 24px; background: var(--black); }
  .card--back .brand__name { font-size: 120px; letter-spacing: 8px; }
  .card--back .brand__sub { font-size: 34px; letter-spacing: 6px; margin-top: 8px; }
</style>
</head>
<body>

  <section class="card card--front" aria-label="Business card, contact side">
    <svg class="bands" width="900" height="514" viewBox="0 0 900 514" aria-hidden="true">
      <defs>
        <linearGradient id="frontCorner" x1="0" y1="0" x2="1" y2="1">
          <stop offset="0" stop-color="#c44a5a"/>
          <stop offset="0.35" stop-color="#0255a3"/>
          <stop offset="0.55" stop-color="#8a7a7a"/>
          <stop offset="0.8" stop-color="#f78f20"/>
        </linearGradient>
      </defs>
      <polygon points="0,0 480,0 0,260" fill="url(#frontCorner)"/>
      <polygon points="480,0 580,0 0,315 0,260" fill="var(--grey-light)"/>
    </svg>

    <div class="brand">
      <span class="brand__mark"></span>
      <span class="brand__text">
        <span class="brand__name">VELMAR</span>
        <span class="brand__sub">CONSTRUCTION LLC</span>
      </span>
    </div>

    <div class="holder">
      <p class="holder__name">Gerald Tomasino</p>
      <p class="holder__cell">M. 555-742-0583</p>
    </div>

    <div class="divider"></div>

    <ul class="contacts">
      <li><span class="contacts__label">T .</span>555-318-6094</li>
      <li><span class="contacts__label">W .</span>velmarllc.Com</li>
      <li><span class="contacts__label">E .</span>velmarllc@tridomail.Com</li>
      <li>418 harbor 87th.</li>
      <li>Dunmoor park ny 10352</li>
    </ul>
  </section>

  <section class="card card--back" aria-label="Business card, logo side">
    <svg class="bands" width="900" height="514" viewBox="0 0 900 514" aria-hidden="true">
      <defs>
        <linearGradient id="backField" x1="0" y1="0.2" x2="1" y2="0.8">
          <stop offset="0" stop-color="#c44a5a"/>
          <stop offset="0.22" stop-color="#0255a3"/>
          <stop offset="0.42" stop-color="#8a7d76"/>
          <stop offset="0.62" stop-color="#f78f20"/>
          <stop offset="1" stop-color="#5a5552"/>
        </linearGradient>
      </defs>
      <rect width="900" height="514" fill="url(#backField)"/>
      <polygon points="0,0 240,0 0,140" fill="#c44a5a"/>
      <polygon points="240,0 490,0 0,250 0,140" fill="var(--grey-light)"/>
    </svg>

    <div class="brand">
      <span class="brand__mark"></span>
      <span class="brand__text">
        <span class="brand__name">VELMAR</span>
        <span class="brand__sub">CONSTRUCTION LLC</span>
      </span>
    </div>
  </section>

</body>
</html>
```